Business is backhoe and truck hire. As the title indicates, we dig dirt. Colours preferred are charcoal, red and or orange. Would like a backhoe on the card,possibly a designs with the silhouette of the machine in the background. I We would like to incorporate a large tick in the title for solutions. I thought it could be part of the "W" . Our shirts are Black polo's with orange lines around sleeves and sides. We are a new business in rural Qld, happy to do the smaller jobs that others wont.

Industry/Entity Type

Business

Contact Information for Business Card

Tall Creek Groundworks Services

Backhoe and Truck Hire
ABN:81264950173

Peter Holloway
PH: 0491 732 580
PH: 0493 618 204
PH: 4683 1057 a/h

email: tcgservices@mailbox-example.net

```html
<!DOCTYPE html>
<html lang="en">
<head>
<meta charset="utf-8">
<title>Tall Creek Groundworks Services – Business Card</title>
<link rel="stylesheet" href="https://fonts.googleapis.com/css2?family=Open+Sans:wght@400;600;700&display=swap">
<style>
  :root {
    --page-bg: #eceded;
    --sky-top: #e41f26;
    --sky-mid: #ef5a2c;
    --sky-bottom: #f8a83e;
    --charcoal: #2b2a29;
    --ink: #3b2622;
    --white: #ffffff;
  }
  * { margin: 0; padding: 0; box-sizing: border-box; }
  html, body {
    width: 1200px;
    height: 806px;
    overflow: hidden;
    background: var(--page-bg);
    font-family: "Open Sans", Arial, sans-serif;
  }
  .business-card {
    position: absolute;
    left: 125px;
    top: 116px;
    width: 950px;
    height: 546px;
    overflow: hidden;
    background: linear-gradient(180deg, var(--sky-top) 0%, var(--sky-mid) 40%, var(--sky-bottom) 78%);
  }
  .company-name {
    position: absolute;
    left: 86px;
    top: 46px;
    font-size: 45px;
    font-weight: 600;
    color: var(--ink);
    letter-spacing: 0.2px;
    white-space: nowrap;
  }
  .abn {
    position: absolute;
    right: 94px;
    top: 112px;
    font-size: 24px;
    color: var(--ink);
  }
  .contact {
    position: absolute;
    left: 487px;
    top: 190px;
    color: var(--ink);
  }
  .contact-name {
    margin-left: 32px;
    font-size: 27px;
    font-weight: 700;
    margin-bottom: 22px;
  }
  .phone-block {
    position: relative;
    padding-left: 34px;
    font-size: 26px;
    line-height: 34px;
  }
  .phone-icon {
    position: absolute;
    left: 0;
    top: 42px;
    width: 22px;
    height: 28px;
  }
  .email-line {
    display: flex;
    align-items: center;
    margin-top: 2px;
    font-size: 26px;
    line-height: 34px;
    white-space: nowrap;
  }
  .email-icon {
    width: 30px;
    height: 20px;
    margin-left: -8px;
    margin-right: 12px;
  }
  .backhoe-illustration {
    position: absolute;
    left: 45px;
    top: 215px;
    width: 430px;
    height: 230px;
    background: linear-gradient(180deg, rgba(43,42,41,0.55) 0%, rgba(43,42,41,0.85) 100%);
    border-radius: 6px;
  }
  .ground-band {
    position: absolute;
    left: 0;
    bottom: 0;
    width: 950px;
    height: 125px;
    background: var(--charcoal);
  }
  .service-line {
    position: absolute;
    left: 0;
    width: 950px;
    top: 455px;
    text-align: center;
    font-size: 44px;
    font-weight: 700;
    color: var(--white);
    letter-spacing: 0.3px;
  }
</style>
</head>
<body>
  <div class="business-card">
    <div class="company-name">Tall Creek Groundworks Services</div>
    <div class="abn">ABN:81264950173</div>

    <div class="contact">
      <div class="contact-name">Peter Holloway</div>
      <div class="phone-block">
        <svg class="phone-icon" viewBox="0 0 22 28" aria-hidden="true">
          <path d="M6 2 L9 8 L6.5 10 Q8 16 12 20 L14.5 18 L19 23 L15.5 26 Q4 22 2 6 Z" fill="none" stroke="#3b2622" stroke-width="2" stroke-linejoin="round"/>
        </svg>
        <div>0491 732 580</div>
        <div>0493 618 204</div>
        <div>4683 1057</div>
      </div>
      <div class="email-line">
        <svg class="email-icon" viewBox="0 0 30 20" aria-hidden="true">
          <rect x="1" y="1" width="28" height="18" fill="none" stroke="#3b2622" stroke-width="2"/>
          <path d="M1 1 L15 12 L29 1" fill="none" stroke="#3b2622" stroke-width="2"/>
        </svg>
        <span>tcgservices@mailbox-example.net</span>
      </div>
    </div>

    <div class="ground-band"></div>
    <div class="backhoe-illustration" role="img" aria-label="Silhouette of a backhoe loader standing on rough ground"></div>
    <div class="service-line">BACKHOE AND TRUCK HIRE</div>
  </div>
</body>
</html>
```